Business Card Design Project

Bold, modern, clean business card design needed. Prefer double sided with art logo on the back. Front of card with company name logo, no art.

Target Market(s)

Our consulting company supports local, state and federal law enforcement officers. Therefore the design should be clean and direct with no flash or arrogance to it.

Industry/Entity Type

Business

```html
<!DOCTYPE html>
<html lang="en">
<head>
<meta charset="utf-8">
<title>Halvern Technologies — Business Card</title>
<link rel="stylesheet" href="https://fonts.googleapis.com/css2?family=Open+Sans:wght@400;600&display=swap">
<style>
  :root {
    --backdrop: #d4d4d6;
    --card: #ffffff;
    --ink: #1b1b1b;
    --ink-soft: #3a3a3a;
    --accent: #8cc63f;
    --rule: #9a9a9a;
    --shadow: rgba(0, 0, 0, 0.22);
  }
  * { box-sizing: border-box; margin: 0; padding: 0; }
  html, body {
    width: 883px;
    height: 1200px;
    overflow: hidden;
    background: var(--backdrop);
    font-family: "Open Sans", Arial, sans-serif;
    color: var(--ink);
  }
  .stage {
    width: 883px;
    height: 1200px;
    display: flex;
    flex-direction: column;
    align-items: center;
    justify-content: center;
    gap: 40px;
  }
  .card {
    position: relative;
    width: 600px;
    height: 340px;
    background: var(--card);
    box-shadow: 0 6px 14px var(--shadow);
  }

  /* Brand lockup */
  .brand {
    display: flex;
    align-items: center;
    gap: 12px;
  }
  .brand-dot {
    width: 30px;
    height: 30px;
    border-radius: 50%;
    background: var(--accent);
    flex: none;
  }
  .brand-name {
    font-weight: 400;
    color: var(--ink);
    letter-spacing: 0.06em;
    text-transform: uppercase;
    white-space: nowrap;
  }

  /* Front */
  .card-front {
    display: flex;
    align-items: center;
    justify-content: center;
  }
  .card-front .brand-name { font-size: 30px; }
  .card-front .brand-dot { width: 38px; height: 38px; }

  /* Back */
  .card-back .brand {
    position: absolute;
    left: 32px;
    top: 70px;
  }
  .card-back .brand-name { font-size: 21px; }
  .holder {
    position: absolute;
    right: 34px;
    top: 170px;
    text-align: right;
  }
  .holder-name {
    color: var(--accent);
    font-size: 22px;
    line-height: 1.1;
  }
  .holder-role {
    font-size: 15px;
    color: var(--ink-soft);
  }
  .divider {
    position: absolute;
    left: 28px;
    right: 34px;
    top: 222px;
    height: 1px;
    background: var(--rule);
  }
  .contacts {
    position: absolute;
    left: 30px;
    top: 234px;
    list-style: none;
    font-size: 15px;
    line-height: 21px;
  }
  .contacts li { display: flex; align-items: center; gap: 12px; }
  .contacts svg { width: 12px; height: 12px; fill: var(--accent); flex: none; }
  .address {
    position: absolute;
    right: 34px;
    top: 234px;
    text-align: right;
    font-size: 15px;
    line-height: 21px;
  }
  .address-line { display: flex; justify-content: flex-end; align-items: center; gap: 8px; }
  .address svg { width: 11px; height: 14px; fill: var(--ink); }
  .address .address-line:last-child { padding-right: 19px; }
</style>
</head>
<body>
<main class="stage">
  <section class="card card-front" aria-label="Card front">
    <div class="brand">
      <span class="brand-dot"></span>
      <span class="brand-name">Halvern Technologies</span>
    </div>
  </section>

  <section class="card card-back" aria-label="Card back">
    <div class="brand">
      <span class="brand-dot"></span>
      <span class="brand-name">Halvern Technologies</span>
    </div>

    <div class="holder">
      <p class="holder-name">your name</p>
      <p class="holder-role">designation</p>
    </div>

    <div class="divider"></div>

    <ul class="contacts">
      <li>
        <svg viewBox="0 0 12 12" aria-hidden="true"><path d="M1 3h10v7H1z M3 1h6v2H3z"/></svg>
        0123 456 789
      </li>
      <li>
        <svg viewBox="0 0 12 12" aria-hidden="true"><path d="M3 0h6v12H3z M4 1.5v8h4v-8z"/></svg>
        0123 456 789
      </li>
      <li>
        <svg viewBox="0 0 12 12" aria-hidden="true"><path d="M0 2h12v8H0z"/><path d="M0 2l6 4 6-4" fill="none" stroke="#fff" stroke-width="1"/></svg>
        youremail@mail.com
      </li>
      <li>
        <svg viewBox="0 0 12 12" aria-hidden="true"><circle cx="6" cy="6" r="6"/></svg>
        www.yourwebsite.com
      </li>
    </ul>

    <div class="address">
      <p class="address-line">
        address (street address
        <svg viewBox="0 0 11 14" aria-hidden="true"><path d="M5.5 0A5.5 5.5 0 0 0 0 5.5C0 9.5 5.5 14 5.5 14S11 9.5 11 5.5A5.5 5.5 0 0 0 5.5 0zm0 7.5a2 2 0 1 1 0-4 2 2 0 0 1 0 4z"/></svg>
      </p>
      <p class="address-line">suite number, city, state, zip</p>
    </div>
  </section>
</main>
</body>
</html>
```